Process Roadmap for Interior Design Firm

We are looking to ramp up the design appeal of our current process roadmap to be very visually interesting, while staying informative and descriptive about our process.

Target Market(s)

In-house Clients

Industry/Entity Type

Interior Design Firm focused on sustainable and holistic design.

Other font styles liked:
• raleway

Requirements
Must have
• 1.) it would be nice if the graphic provided a more clear indication of the “journey” from one step to the next, so that there was a clear sense of the progression (such that we are directing the viewer) 2.). We would want it to fit on an 8.5”x11” page (the page could be horizontal when we have the Calm Compass formatted out with the testimonials) (in addition to the testimonials, we may also want to have the detailed descriptions of each step of the process presented below the graphic, so that the graphic is cleaner) 3.) ideally the graphic is clear and simple enough to also be used on our Bi-Weekly Client Updates, which will be typed updates for clients re their project budgets, schedule and scope. The Calm Compass graphic (without all the testimonials) would be at the end of the update, and would fit on the page horizontally at the bottom, perhaps in a space which is 7.5”w x 4”h or so.
Should not have
• bold or bright colors. Natural neutrals are preferred, such as the ones featured on the provided graphic.

```html
<!DOCTYPE html>
<html lang="en">
<head>
<meta charset="utf-8">
<title>MHI Calm Compass</title>
<link href="https://fonts.googleapis.com/css2?family=Raleway:wght@500&family=Roboto:ital,wght@0,300;0,400;0,500;0,700;1,400&display=swap" rel="stylesheet">
<style>
:root{
  --sand-top:#cbbba5;
  --sand-bottom:#e6ddcf;
  --path-light:#f2eee8;
  --path-shade:#e1d8cc;
  --icon-fill:#ece4d9;
  --copper:#b07c4a;
  --ink:#4f4a45;
  --ink-soft:#7a746d;
  --paper:#ffffff;
}
*{margin:0;padding:0;box-sizing:border-box}
html,body{width:1200px;height:927px;overflow:hidden;background:var(--paper)}
.sheet{position:relative;width:1200px;height:927px;overflow:hidden;
  background:linear-gradient(180deg,var(--sand-top) 0%,var(--sand-bottom) 80%);
  font-family:'Roboto',sans-serif;color:var(--ink)}
.art{position:absolute;left:0;top:0}
.brand{position:absolute;left:44px;top:26px;width:226px;height:101px;background:var(--paper);
  display:flex;align-items:center;gap:14px;padding-left:18px}
.brand-mark{width:22px;height:22px;background:var(--copper)}
.brand-name{font-family:'Raleway',sans-serif;font-weight:500;font-size:17px;letter-spacing:2px;color:var(--copper);line-height:1.3;text-transform:uppercase}
.title{position:absolute;left:604px;top:52px;font-size:52px;font-weight:400;letter-spacing:.5px;color:var(--ink);line-height:1}
.title b{font-weight:700;letter-spacing:-1px}
.step-icon{position:absolute;width:76px;height:76px;border-radius:50%;background:var(--icon-fill)}
.step-label{position:absolute;width:120px;text-align:center;font-weight:500;font-size:20px;color:var(--ink);top:296px}
.step{position:absolute;top:486px;width:148px}
.step-num{font-size:50px;line-height:1;color:var(--copper);letter-spacing:-1px;margin-left:-4px}
.step-num .light{font-weight:300}
.step-num .bold{font-weight:700}
.step p{font-size:14px;line-height:16.6px;color:var(--ink);margin-top:4px;letter-spacing:-.1px}
.step hr{width:27px;border:0;border-top:1.5px solid var(--copper);margin:6px 0 7px}
.testimonials-title{position:absolute;left:52px;top:722px;font-size:28px;font-weight:700;letter-spacing:1px;color:var(--ink);line-height:34px}
.testimonials-title span{color:var(--sand-top);font-size:64px;line-height:0;vertical-align:-24px;margin-left:10px;font-weight:700}
.quote{position:absolute;top:775px;width:262px;font-size:14px;line-height:16.4px;font-weight:300;color:var(--ink-soft);letter-spacing:-.1px}
.quote cite{display:block;font-style:italic;font-weight:400;color:var(--ink);margin-top:2px}
</style>
</head>
<body>
<main class="sheet">
<svg class="art" width="1200" height="927" viewBox="0 0 1200 927" aria-hidden="true">
  <line x1="0" y1="76" x2="592" y2="76" stroke="var(--copper)" stroke-width="2"/>
  <line x1="1150" y1="76" x2="1200" y2="76" stroke="var(--copper)" stroke-width="2"/>
  <path d="M0 700 H300 Q318 700 330 713 L357 745 H1105 C1170 745 1200 690 1200 615 V927 H0 Z" fill="var(--paper)"/>
  <path d="M78 198 V379 A75 75 0 0 0 228 379 V240 A75 75 0 0 1 377 240 V379 A75 75 0 0 0 526 379 V240 A75 75 0 0 1 676 240 V379 A75 75 0 0 0 825 379 V240 A75 75 0 0 1 976 240 V379 A75 75 0 0 0 1125 379 V239" fill="none" stroke="var(--path-light)" stroke-width="38"/>
  <g fill="none" stroke="var(--path-shade)" stroke-width="38">
    <path d="M228 250 V240 A75 75 0 0 1 302 165"/>
    <path d="M377 380 V240 A75 75 0 0 0 302 165"/>
    <path d="M526 250 V240 A75 75 0 0 1 601 165"/>
    <path d="M676 380 V240 A75 75 0 0 0 601 165"/>
    <path d="M676 380 A75 75 0 0 0 750 454"/>
    <path d="M825 250 V240 A75 75 0 0 1 900 165"/>
    <path d="M976 380 V240 A75 75 0 0 0 900 165"/>
  </g>
  <polygon points="44,163 112,163 78,190" fill="#ece6dd"/>
  <circle cx="1125" cy="225" r="24" fill="#e3dbd0"/>
  <circle cx="1125" cy="220" r="21" fill="var(--copper)"/>
  <path d="M1114 220 l7 7 l13 -14" fill="none" stroke="#fff" stroke-width="4" stroke-linecap="round" stroke-linejoin="round"/>
  <g stroke="var(--copper)" stroke-width="1.5">
    <line x1="112" y1="279" x2="194" y2="279"/><line x1="260" y1="337" x2="342" y2="337"/>
    <line x1="409" y1="279" x2="491" y2="279"/><line x1="559" y1="337" x2="641" y2="337"/>
    <line x1="707" y1="279" x2="789" y2="279"/><line x1="858" y1="337" x2="940" y2="337"/>
    <line x1="1009" y1="279" x2="1091" y2="279"/>
  </g>
</svg>

<div class="step-icon" role="img" aria-label="Listening icon" style="left:115px;top:332px"></div>
<div class="step-icon" role="img" aria-label="Visioning icon" style="left:264px;top:212px"></div>
<div class="step-icon" role="img" aria-label="Planning icon" style="left:413px;top:334px"></div>
<div class="step-icon" role="img" aria-label="Designing icon" style="left:563px;top:209px"></div>
<div class="step-icon" role="img" aria-label="Managing icon" style="left:712px;top:334px"></div>
<div class="step-icon" role="img" aria-label="Installing icon" style="left:860px;top:205px"></div>
<div class="step-icon" role="img" aria-label="Completing icon" style="left:1012px;top:338px"></div>

<div class="brand"><span class="brand-mark"></span><span class="brand-name">Marlowe Hart<br>Interiors</span></div>
<h1 class="title"><b>MHI</b> CALM COMPASS</h1>

<div class="step-label" style="left:93px">Listening</div>
<div class="step-label" style="left:241px">Visioning</div>
<div class="step-label" style="left:389px">Planning</div>
<div class="step-label" style="left:540px">Designing</div>
<div class="step-label" style="left:688px">Managing</div>
<div class="step-label" style="left:838px">Installing</div>
<div class="step-label" style="left:989px">Completing</div>

<section class="step" style="left:69px">
  <div class="step-num"><span class="light">0</span><span class="bold">1</span></div>
  <p>Listening to our clients their land, and their home.</p><hr>
  <p>Identifying their needs, challenges, wishes, and dreams.</p>
</section>
<section class="step" style="left:230px">
  <div class="step-num"><span class="light">0</span><span class="bold">2</span></div>
  <p>Facilitating a guided visioning process to clarify the deepest intention, true purpose, and highest potential for their home and their future within it.</p>
</section>
<section class="step" style="left:382px">
  <div class="step-num"><span class="light">0</span><span class="bold">3</span></div>
  <p>Turning our client’s vision into a clearly defined scope, budget and timeline.</p><hr>
  <p>Mapping out the steps for making their dream a reality.</p><hr>
  <p>Setting a meeting schedule from start to finish.</p>
</section>
<section class="step" style="left:534px">
  <div class="step-num"><span class="light">0</span><span class="bold">4</span></div>
  <p>Following the schedule through the design phases, from initial design concepts, technical drawings and details, and the selection of all finishes, fixtures and furnishings.</p>
</section>
<section class="step" style="left:695px">
  <div class="step-num"><span class="light">0</span><span class="bold">5</span></div>
  <p>Coordinating with clients, builders, architects and vendors, to ensure that the design is executed with excellence, and the construction and the furnishings are on-time and on-budget.</p>
</section>
<section class="step" style="left:848px">
  <div class="step-num"><span class="light">0</span><span class="bold">6</span></div>
  <p>Overseeing the inspection, installation and arrangements of all furnishings, lighting, artwork and decorative items.</p><hr>
  <p>Taking care of every last detail.</p>
</section>
<section class="step" style="left:1003px">
  <div class="step-num"><span class="light">0</span><span class="bold">7</span></div>
  <p>Fixing any issues or defects.</p><hr>
  <p>Follow up on all remaining items.</p><hr>
  <p>Completing the final finishing touches to our client's full and total satisfaction.</p>
</section>

<h2 class="testimonials-title">TESTIMONIALS<span>“</span></h2>
<blockquote class="quote" style="left:53px">“Lorem ipsum dolor sit amet, consectetuer adipiscing elit, sed diam nonummy nibh euismod tincidunt ut laoreet dolore magna aliquam erat volutpat. Ut wisi enim ad minim veniam, quis nostrud exerci tation ullamcorper.”<cite>John Doe</cite></blockquote>
<blockquote class="quote" style="left:330px">“Lorem ipsum dolor sit amet, consectetuer adipiscing elit, sed diam nonummy nibh euismod tincidunt ut laoreet dolore magna aliquam erat volutpat. Ut wisi enim ad minim veniam, quis nostrud exerci tation ullamcorper.”<cite>John Doe</cite></blockquote>
<blockquote class="quote" style="left:616px">“Lorem ipsum dolor sit amet, consectetuer adipiscing elit, sed diam nonummy nibh euismod tincidunt ut laoreet dolore magna aliquam erat volutpat. Ut wisi enim ad minim veniam, quis nostrud exerci tation ullamcorper.”<cite>John Doe</cite></blockquote>
<blockquote class="quote" style="left:889px">“Lorem ipsum dolor sit amet, consectetuer adipiscing elit, sed diam nonummy nibh euismod tincidunt ut laoreet dolore magna aliquam erat volutpat. Ut wisi enim ad minim veniam, quis nostrud exerci tation ullamcorper.”<cite>John Doe</cite></blockquote>
</main>
</body>
</html>
```